GUARANTEED! - Creation of Lumora Promotional Images (requires Photoshops to modify cars)

Hi all,

We will require 5 different images to be created although once the first one is completed, the look and theme can literally be copied across to the others. These promotional images are to represent the service our website offers as well as the benefit’s the user can receive. (please ask for the website via private message if required) Our website is literally a comparison website related to vehicle modifications - so we make it quick and easy for users to find the best deal with local Window Tinters, ECU Remappers, Alloy Wheel Refurbs & More.

Aim of the image - This is purely to be posted on lumora to push viewers to our website / lumora page (there will be links in the description when it’s posted on lumora) so the image needs to tell the user what we do and urge them to visit the website.

Target market - our target market is mainly the car enthusiast (ages between 17 - 25) although we’re looking to keep this promotional image simple, professional and with the use of light neutral colours.

Image to be created - (our idea, please feel free to change) - see attachment of rough sketch created titled : ‘Rough Sketch Promotional Image

Main title across the top will read ‘FIND THE BEST DEAL WITH :’ - The words best deal should stand out more and be of a larger font / potentially different colour, maybe orange to keep in theme with the website. Then as shown in the sketch, we will have car number 1 which has been photoshopped as stated further down . Then we will have arrows pointing onto the car which will state the different modifications that has been completed on the car e.g - arrow will point to the rear window and will state the words :

WINDOW TINTERS
IN YOUR AREA

(regarding the text stated above, we feel it would be best if they were all placed the same distance away from the car to keep the professional look) - we also feel the service mentioned such as ‘WINDOW TINTERS’ should be a larger font than the ‘IN YOUR AREA’

Each car will have 4 arrows pointing on different parts of the car with text added as stated above (hopefully the rough sketch will make all these requirements that little bit clearer)

Then underneath the car image with the 4 arrows and text, we will have a Call to action button (which should keep the same kind of theme as that on the website homepage, (green blackground of block with white text) - The text in this button will read ‘CLICK BELOW!’ - we also had the idea of adding an arrow under the Call to action button to point the users to the description below the image. (Needs to be clear space around the CTA so it stands out - apart from potentially this arrow)

Then finally we’d like to have our logo (quite small) to the bottom left of the image with the words ‘PLEASE SHARE!’ to the bottom right of the image.

As you can see, the requirements we’re after are quite simple so the time will be mostly in the photoshopping of the 5 cars.

Please refer to the rough sketch but if you have any questions, please contact us here.

PHOTOSHOPS REQUIRED

The changes made to each car will be partly left up to you - however it’s vitally important that it stands out yet doesn’t look ‘silly’ and needs to look realistic - looking realistic is important.

Photoshop requirements

Car 1 - Green Valtero

- Possibly change colour - please feel free to try other colours (need to look realistic)
- Change the colour of the rear window to a limo style black.
- Change the colour of the roof (can only see a slight bit of it) to black
- Change the colour of the wheels (the colour used here will depend on the change colour of the actual car, some options we like include yellow, green, orange and red

Car 2 - White Korvel ZX

- Change the colour of the rear window and rear side window to a limo style black
- Change the colour of the roof to black (not decided whether it should be black/matt black so test)
- Change the colour of the wheels to a red/ orange

Car 3 - Blue Brenn

- Possibly change colour - please feel free to try other colours - maybe a red but needs to look realistic
- Change the colour of the rear window visible to a limo style black
- Change the colour of the roof to black
- Change the colour of the wheels to black

Car 4 - Yellow Korvel ZX

- Please try changing the colour of this to a metallic grey/dark silver / gloss dark blue.
- Change the colour of the wheels to a yellow

Car 5 - Black Korvel ZX (first of all we need to remove the background of this image)

Please state if this is too difficult to photoshop and we’ll go from there.

- Colour change to red please - ensure looks realistic
- Change the colour of the wheels to a black

If any of the changes we’ve requested don’t look realistic when you’ve created them - please let us know and feel free to try other colours … remember, needs to look professional and realistic.

Background - up to you although we feel something quite neutral would work well - please however try out whatever you think would look good.

************* IMPORTANT - PLEASE READ *******************

To save you time and to avoid wasted effort, we'd like you to create the promotional image using image 1 ONLY first of all - once we're satisfied with that 100%, we would then ask you to complete the other 4 images (which shouldn't take long once the first image is complete)

*************************************************************************

Just to add - we have purchased the rights for these images but if you feel you've some car images that would suit our requirements better than these, please send them across to us for our opinion.

We may add to this brief so keep an eye out - we will also offer additional work to the winning designer - if you have any questions at all, please ask away.

Thanks,

Owen,

Still not there with the design all - keep them coming.Thanks Added Saturday, October 1, 2016

Project Deadline Extended Reason: Not happy with the designs receivec and only received a few different designers whereas the project I purchased stated I would receive alot more..Not impressed so far.Regards.Owen Added Monday, October 3, 2016

Car enthusiast / youthful - but needs to have the professional clear look - most important.

Promotional

Serif
Sans Serif

• - Title of 'FIND THE BEST DEAL WITH : '
• - Car image for each
• - 4 Arrows coming off car for each image with the text stated
• - Call to action button - that stands out
• - Logo and words 'Please share!' / 'Please share me!'
• Potential other car images (would need commercial right so would have to be free for commercial use or a suitable price to pay for the rights) - this is only if you feel you have an image that would be better than those we currently have.
• Needs to be kept clear - points to stand out are the opening title of 'FIND THE BEST DEAL WITH :', Car and the service such as 'WINDOW TINTERS'

```html
<!DOCTYPE html>
<html lang="en">
<head>
<meta charset="UTF-8">
<title>Find the Best Deal – Tune Nearby</title>
<link rel="stylesheet" href="https://fonts.googleapis.com/css2?family=Exo+2:ital,wght@1,800;1,900&family=Orbitron:wght@700;800&display=swap">
<style>
  :root {
    --ink: #111111;
    --slate: #3a4048;
    --orange: #ff7a12;
    --label-bg: #e2e3e4;
    --page: #ffffff;
    --page-tint: #f4f4f4;
    --green-top: #2fc42a;
    --green-bottom: #129a14;
    --white: #ffffff;
    --photo-light: #fbe3cf;
    --photo-mid: #f6a15e;
  }
  html, body {
    margin: 0;
    padding: 0;
    overflow: hidden;
    background: var(--page);
  }
  .poster {
    position: relative;
    width: 1200px;
    height: 1200px;
    overflow: hidden;
    background: linear-gradient(180deg, var(--page-tint) 0%, var(--page) 45%, var(--page-tint) 100%);
    font-family: "Orbitron", sans-serif;
    color: var(--ink);
  }
  .headline {
    position: absolute;
    left: 0;
    top: 62px;
    width: 1200px;
    margin: 0;
    text-align: center;
    font-family: "Exo 2", sans-serif;
    font-style: italic;
    font-weight: 900;
    white-space: nowrap;
    line-height: 1;
  }
  .headline .plain {
    font-size: 64px;
    color: var(--ink);
    display: inline-block;
    border-bottom: 4px solid var(--ink);
    padding-bottom: 8px;
    letter-spacing: -1px;
  }
  .headline .accent {
    font-size: 88px;
    color: var(--orange);
    margin: 0 18px;
    letter-spacing: -1px;
  }
  .car-photo {
    position: absolute;
    left: 150px;
    top: 395px;
    width: 940px;
    height: 390px;
    border-radius: 8px;
    background: radial-gradient(ellipse at 50% 55%, var(--photo-mid) 0%, var(--photo-light) 70%, var(--page) 100%);
  }
  .connectors {
    position: absolute;
    inset: 0;
    pointer-events: none;
  }
  .service {
    position: absolute;
    background: var(--label-bg);
    height: 86px;
    box-sizing: border-box;
    padding-top: 15px;
    white-space: nowrap;
  }
  .service .name {
    display: block;
    font-size: 24px;
    font-weight: 800;
    letter-spacing: 1.5px;
    line-height: 1;
    color: var(--ink);
  }
  .service .area {
    display: block;
    font-size: 16px;
    font-weight: 700;
    letter-spacing: 1.5px;
    line-height: 1;
    color: var(--slate);
    margin-top: 12px;
  }
  .service--tint {
    left: 92px; top: 250px; width: 378px;
    padding-left: 14px;
    clip-path: polygon(0 0, 89% 0, 100% 100%, 0 100%);
  }
  .service--roof {
    left: 605px; top: 250px; width: 513px;
    padding-left: 15px;
    clip-path: polygon(0 0, 92% 0, 100% 100%, 0 100%);
  }
  .service--wheels {
    left: 92px; top: 786px; width: 561px;
    padding-right: 16px;
    padding-top: 19px;
    text-align: right;
    clip-path: polygon(7% 0, 100% 0, 100% 100%, 0 100%);
  }
  .service--ecu {
    left: 768px; top: 786px; width: 352px;
    padding-right: 12px;
    padding-top: 19px;
    text-align: right;
    clip-path: polygon(12% 0, 100% 0, 100% 100%, 0 100%);
  }
  .cta {
    position: absolute;
    left: 360px;
    top: 951px;
    width: 491px;
    height: 108px;
    border-radius: 6px;
    background: linear-gradient(180deg, var(--green-top), var(--green-bottom));
    color: var(--white);
    font-family: "Exo 2", sans-serif;
    font-style: italic;
    font-weight: 800;
    font-size: 48px;
    letter-spacing: 1px;
    display: flex;
    align-items: center;
    justify-content: center;
  }
  .cta-pointer {
    position: absolute;
    left: 563px;
    top: 1088px;
  }
  .brand {
    position: absolute;
    left: 64px;
    top: 1126px;
    font-family: "Exo 2", sans-serif;
    font-style: italic;
    font-weight: 900;
    font-size: 24px;
    letter-spacing: 1px;
    color: var(--ink);
  }
  .share {
    position: absolute;
    left: 962px;
    top: 1104px;
    display: flex;
    align-items: center;
    gap: 16px;
  }
  .share-text {
    font-family: "Exo 2", sans-serif;
    font-style: italic;
    font-weight: 900;
    font-size: 32px;
    line-height: 1.05;
    color: var(--slate);
    text-align: right;
  }
</style>
</head>
<body>
<main class="poster">
  <h1 class="headline">
    <span class="plain">FIND THE</span><span class="accent">BEST DEAL</span><span class="plain">WITH:</span>
  </h1>

  <div class="car-photo" role="img" aria-label="Photo of an orange three-door hatchback with black roof, limo-tinted windows and orange alloy wheels"></div>

  <svg class="connectors" width="1200" height="1200" viewBox="0 0 1200 1200" aria-hidden="true">
    <g fill="none" stroke="#3a4048" stroke-width="4">
      <polyline points="470,337 94,337 94,461 214,461"/>
      <polyline points="1117,339 607,339 607,384"/>
      <polyline points="132,785 652,785 652,764"/>
      <polyline points="1118,785 1118,552 1048,552"/>
    </g>
    <g fill="#3a4048">
      <polygon points="224,461 206,450 210,461 206,472"/>
      <polygon points="607,394 596,376 607,380 618,376"/>
      <polygon points="652,754 641,772 652,768 663,772"/>
      <polygon points="1038,552 1056,541 1052,552 1056,563"/>
    </g>
  </svg>

  <div class="service service--tint">
    <span class="name">WINDOW TINTERS</span>
    <span class="area">IN YOUR AREA</span>
  </div>
  <div class="service service--roof">
    <span class="name">ROOF VINYL WRAPPERS</span>
    <span class="area">IN YOUR AREA</span>
  </div>
  <div class="service service--wheels">
    <span class="name">ALLOY WHEEL REFURBERS</span>
    <span class="area">IN YOUR AREA</span>
  </div>
  <div class="service service--ecu">
    <span class="name">ECU REMAPPERS</span>
    <span class="area">IN YOUR AREA</span>
  </div>

  <div class="cta">SEARCH FOR FREE</div>
  <svg class="cta-pointer" width="94" height="80" viewBox="0 0 94 80" aria-hidden="true">
    <polygon points="0,0 47,24 94,0 47,80" fill="#22b421"/>
  </svg>

  <div class="brand">TUNE NEARBY</div>

  <div class="share">
    <svg width="50" height="54" viewBox="0 0 50 54" aria-hidden="true">
      <g stroke="#2fb52c" stroke-width="6">
        <line x1="38" y1="10" x2="12" y2="27"/>
        <line x1="12" y1="27" x2="38" y2="44"/>
      </g>
      <g fill="#2fb52c">
        <circle cx="38" cy="10" r="9"/>
        <circle cx="12" cy="27" r="9"/>
        <circle cx="38" cy="44" r="9"/>
      </g>
    </svg>
    <div class="share-text">PLEASE<br>SHARE</div>
  </div>
</main>
</body>
</html>
```